Hello - we need a label design for our Corvane Medical Hair Loss supplement. It is a natural hair loss supplement for black/african american women to regrow new hair and help restore hair loss & thinning hair due to vitamin deficiencies, traction alopecia, etc. It is a science based efficacious supplement with a centuries old medicinal herbal formula.
Attached is the logo & files of other generic competition and also Black hair products for your perusal. The label has to be a upscale and have an ethnic flair to it. The product is clinically effective, leveraged by Ancient Wisdom and Modern Science. The front of the label should include the following:
Corvane Medical (logo)
Crown Catalyst
Advanced Women’s Hair Loss Formula
TRACTION ALOPECIA THERAPY
- Prevents hair loss & restores thinning, fragile hair
- Promotes Natural Hair Growth
- Strengthens Hair for less breakage
- Visibly increases hair density & thickness
- Thicker, Stronger, Longer, Hydrated hair
- Promotes Follicle regeneration & Hair Growth
Site-Specific for hair loss & stunted growth
60 capsules 30-day supply
Target Market(s)
Black/African American Women

```html
<!DOCTYPE html>
<html lang="en">
<head>
<meta charset="utf-8">
<title>Corvane Medical – Crown Catalyst Label</title>
<link rel="stylesheet" href="https://fonts.googleapis.com/css2?family=Montserrat:wght@500;600;700;800&display=swap">
<style>
  :root {
    --page: #f4f4f4;
    --label-black: #0d0d0d;
    --copper: #c9782f;
    --copper-light: #e0a35c;
    --copper-dark: #8a4a1c;
    --band-mid: #b8641f;
    --band-edge: #9c5219;
    --ink-dark: #2a1608;
    --white: #ffffff;
  }
  * { box-sizing: border-box; margin: 0; padding: 0; }
  html, body {
    width: 1200px; height: 1000px; overflow: hidden;
    background: var(--page);
    font-family: "Montserrat", sans-serif;
  }
  .label {
    position: absolute; left: 200px; top: 70px;
    width: 800px; height: 860px;
    background: var(--label-black);
    overflow: hidden;
  }
  .brand {
    position: absolute; top: 122px; left: 0; right: 0; height: 48px;
    display: flex; align-items: center; justify-content: center; gap: 14px;
  }
  .brand-dot {
    width: 20px; height: 20px; border-radius: 50%;
    background: var(--copper);
  }
  .brand-name {
    color: var(--copper-light);
    font-weight: 600; font-size: 36px; letter-spacing: 1px; line-height: 1;
  }
  .product-pill {
    position: absolute; top: 256px; left: 180px;
    width: 440px; height: 66px; border-radius: 14px;
    background: linear-gradient(90deg, var(--copper-dark), var(--copper) 35%, var(--copper-light) 60%, var(--copper) 85%, var(--copper-dark));
    display: flex; align-items: center; justify-content: center;
    color: var(--white); font-weight: 700; font-size: 32px; line-height: 1;
  }
  .headline {
    position: absolute; left: 0; right: 0; text-align: center;
    color: var(--white); font-weight: 800; font-size: 21px; line-height: 26px;
    text-transform: uppercase;
  }
  .headline--first { top: 356px; }
  .headline--second { top: 402px; }
  .rule {
    position: absolute; top: 452px; left: 290px; width: 220px; height: 2px;
    background: var(--white);
  }
  .pattern-band {
    position: absolute; top: 468px; left: 0; width: 800px; height: 276px;
    background: linear-gradient(90deg, var(--band-edge), var(--band-mid) 30%, var(--copper) 50%, var(--band-mid) 70%, var(--band-edge));
  }
  .benefits {
    position: absolute; top: 502px; left: 0; right: 0;
    list-style: none; text-align: center;
    color: var(--ink-dark); font-weight: 600; font-size: 20px; line-height: 34px;
  }
  .label-footer {
    position: absolute; bottom: 0; left: 0; width: 800px; height: 116px;
    background: var(--label-black);
    display: flex; align-items: center; justify-content: space-between;
    padding: 0 36px;
    color: var(--white); font-weight: 700;
  }
  .clinical { display: flex; align-items: center; gap: 10px; font-size: 19px; }
  .supply { font-size: 24px; }
  .supply small { font-size: 17px; font-weight: 600; margin-left: 6px; }
</style>
</head>
<body>
  <section class="label">
    <div class="brand">
      <span class="brand-dot"></span>
      <span class="brand-name">Corvane Medical</span>
    </div>

    <div class="product-pill">Crown Catalyst</div>

    <p class="headline headline--first">Advanced Women's Hair Loss Formula</p>
    <p class="headline headline--second">Traction Alopecia Therapy</p>
    <div class="rule"></div>

    <div class="pattern-band" role="img" aria-label="Band of African geometric pattern in copper and burnt orange tones"></div>
    <ul class="benefits">
      <li>Prevents hair loss &amp; restores thinning, fragile hair</li>
      <li>Promotes Natural Hair Growth</li>
      <li>Strengthens Hair for less breakage</li>
      <li>Visibly increases hair density &amp; thickness</li>
      <li>Thicker, Stronger, Longer, Hydrated hair</li>
      <li>Promotes Follicle regeneration &amp; Hair Growth</li>
    </ul>

    <footer class="label-footer">
      <span class="clinical">Clinically tested
        <svg width="22" height="22" viewBox="0 0 22 22" aria-hidden="true">
          <path d="M4 11.5l4.5 4.5L18 6" fill="none" stroke="#ffffff" stroke-width="2.5" stroke-linecap="round" stroke-linejoin="round"/>
        </svg>
      </span>
      <span class="supply">60 capsules<small>30-day supply</small></span>
    </footer>
  </section>
</body>
</html>
```